We are an integrated facilities management company.

We aggregate everything related to facilities maintenance. Repair-replacement of equipment and facility space materials from:
Asset gathering and tracking.
Vendor screening, contracting and management.
Service requirement development.
Work order processing and management.
Invoice reconciliation.
Vendor payment.
Reporting.
Capital equipment bids and project management.

Target Market(s)

Retail, hospitality, multi-family housing, long term healthcare.

Industry/Entity Type

Maintenance

Contact Information for Business Card

Professional and bold look. (see logo zip file)

Colors
3377b5
85abd2
cedeed

Requirements
Must have
• N/A
Nice to have
• N/A
Should not have
• N/A

```html
<!DOCTYPE html>
<html lang="en">
<head>
<meta charset="utf-8">
<title>Keystone Facility Partners – Business Card</title>
<link href="https://fonts.googleapis.com/css2?family=Montserrat:wght@600;700&family=Open+Sans:ital,wght@0,400;0,700;0,800;1,400&display=swap" rel="stylesheet">
<style>
  :root {
    --brand-blue: #0b56a4;
    --brand-grey: #6a6a6a;
    --text-grey: #4a4a4a;
    --paper: #ffffff;
    --backdrop: #2b2b2b;
  }
  * { box-sizing: border-box; margin: 0; padding: 0; }
  html, body {
    width: 1200px; height: 900px; overflow: hidden;
    background: var(--backdrop);
  }
  .canvas {
    position: relative; width: 1200px; height: 900px;
  }
  .card {
    position: absolute; left: 250px; width: 700px; height: 400px;
    box-shadow: 0 10px 30px rgba(0,0,0,.45);
  }
  .card--back { top: 36px; background: var(--brand-blue); }
  .card--front { top: 464px; background: var(--paper); }

  .wordmark {
    position: absolute; left: 0; right: 0;
    display: flex; align-items: center; justify-content: center; gap: 14px;
  }
  .wordmark__square { width: 22px; height: 22px; }
  .wordmark__name {
    font-family: "Montserrat", sans-serif; font-weight: 700;
    font-size: 34px; letter-spacing: 0.5px; text-transform: uppercase;
  }
  .tagline {
    position: absolute; left: 0; right: 0; text-align: center;
    font-family: "Montserrat", sans-serif; font-weight: 600;
    font-size: 11px; letter-spacing: 5px; text-transform: uppercase;
  }

  .card--back .wordmark { top: 170px; }
  .card--back .wordmark__square { background: var(--paper); }
  .card--back .wordmark__name { color: var(--paper); }
  .card--back .tagline { top: 222px; color: #9dbde0; }

  .card--front .wordmark { top: 80px; }
  .card--front .wordmark__square { background: var(--brand-blue); }
  .card--front .wordmark__name { color: var(--brand-blue); }
  .card--front .tagline { top: 132px; color: #9a9a9a; }

  .person {
    position: absolute; top: 240px; right: 400px; text-align: right;
    font-family: "Open Sans", sans-serif;
  }
  .person__name {
    color: var(--brand-blue); font-weight: 800; font-style: italic;
    font-size: 26px; text-transform: uppercase; letter-spacing: 0.5px;
  }
  .person__title {
    color: var(--brand-grey); font-style: italic; font-size: 20px; margin-top: 2px;
  }
  .divider {
    position: absolute; left: 318px; top: 236px; width: 2px; height: 84px;
    background: var(--brand-blue);
  }
  .contacts {
    position: absolute; left: 336px; top: 232px; list-style: none;
    font-family: "Open Sans", sans-serif; font-size: 21px; color: var(--text-grey);
  }
  .contacts li { display: flex; align-items: center; gap: 10px; height: 30px; }
  .contacts svg { width: 16px; height: 16px; fill: var(--brand-blue); flex: none; }
  .footer-band { position: absolute; left: 0; bottom: 0; width: 700px; height: 22px; }
</style>
</head>
<body>
<main class="canvas">
  <section class="card card--back" aria-label="Card back">
    <div class="wordmark">
      <span class="wordmark__square"></span>
      <span class="wordmark__name">Keystone Facility Partners</span>
    </div>
    <p class="tagline">Maintain · Repair · Replace</p>
  </section>

  <section class="card card--front" aria-label="Card front">
    <div class="wordmark">
      <span class="wordmark__square"></span>
      <span class="wordmark__name">Keystone Facility Partners</span>
    </div>
    <p class="tagline">Maintain · Repair · Replace</p>

    <div class="person">
      <p class="person__name">Dana Whitlock</p>
      <p class="person__title">President</p>
    </div>
    <span class="divider"></span>
    <ul class="contacts">
      <li>
        <svg viewBox="0 0 24 24" aria-hidden="true"><path d="M6.6 10.8a15.1 15.1 0 0 0 6.6 6.6l2.2-2.2c.3-.3.7-.4 1-.2 1.1.4 2.3.6 3.6.6.6 0 1 .4 1 1V20c0 .6-.4 1-1 1A17 17 0 0 1 3 4c0-.6.4-1 1-1h3.5c.6 0 1 .4 1 1 0 1.3.2 2.5.6 3.6.1.3 0 .7-.2 1z"/></svg>
        <span>555-018-2740</span>
      </li>
      <li>
        <svg viewBox="0 0 24 24" aria-hidden="true"><path d="M2 5h20v2l-10 6L2 7z"/><path d="M2 9l10 6 10-6v10H2z"/></svg>
        <span>info@keystonefp.com</span>
      </li>
      <li>
        <svg viewBox="0 0 24 24" aria-hidden="true"><circle cx="12" cy="12" r="10"/></svg>
        <span>www.keystonefp.com</span>
      </li>
    </ul>

    <svg class="footer-band" viewBox="0 0 700 22" aria-hidden="true">
      <polygon points="0,0 380,14 366,22 0,22" fill="var(--brand-blue)"/>
      <polygon points="386,14 700,22 700,22 372,22" fill="var(--brand-grey)"/>
      <rect x="0" y="12" width="368" height="10" fill="var(--brand-blue)"/>
      <rect x="376" y="14" width="324" height="8" fill="var(--brand-grey)"/>
    </svg>
  </section>
</main>
</body>
</html>
```